Business Card Revision

Need to redesign my business cards for a new professional look. We are a courier company. You can go to www.qvrunners.com to see what we do. The trucks have an old company name (Sprout) on them but that is the company we are just now
changing the name.

Target Market(s)

Potential clients. We service the automotive, plumbing, printing, air freight industries as well as many others.

Industry/Entity Type

Business

Contact Information for Business Card

QVmotion
20864 Lark Fenmore Parkway
Cincinnati, Oh 45873

Thomas R. Wendall
President

tom@qvrunners.com

Main: (513) 555-0147

```html
<!DOCTYPE html>
<html lang="en">
<head>
<meta charset="utf-8">
<title>QVmotion Business Card</title>
<link rel="stylesheet" href="https://fonts.googleapis.com/css2?family=Arimo:wght@400;700&display=swap">
<style>
  :root {
    --brand-blue: #1a6fb8;
    --brand-blue-dark: #0e4f8a;
    --brand-blue-light: #2f86cc;
    --brand-green: #2fa445;
    --ink-grey: #555a60;
    --card-white: #ffffff;
    --card-shade: #eef0f2;
    --backdrop: #e4e6e8;
  }
  * { box-sizing: border-box; margin: 0; padding: 0; }
  html, body { width: 1200px; height: 950px; overflow: hidden; }
  body {
    background: var(--backdrop);
    font-family: "Arimo", Arial, sans-serif;
    position: relative;
  }
  .card {
    position: absolute;
    left: 250px;
    width: 700px;
    height: 400px;
    overflow: hidden;
    box-shadow: 0 6px 18px rgba(0,0,0,0.18);
  }
  /* Back side */
  .card-back {
    top: 50px;
    background: linear-gradient(135deg, var(--brand-blue-light) 0%, var(--brand-blue) 50%, var(--brand-blue-dark) 100%);
    color: var(--card-white);
  }
  .card-back .brand-name {
    position: absolute;
    left: 0; right: 0; top: 150px;
    text-align: center;
    font-size: 56px;
    font-weight: 700;
    letter-spacing: 4px;
    color: var(--card-white);
  }
  .card-back .brand-web {
    position: absolute;
    left: 0; right: 0; top: 240px;
    text-align: center;
    font-size: 20px;
    letter-spacing: 5px;
    color: rgba(255,255,255,0.75);
  }
  /* Front side */
  .card-front {
    top: 500px;
    background: linear-gradient(180deg, var(--card-white) 0%, var(--card-white) 60%, var(--card-shade) 100%);
  }
  .person-name {
    position: absolute;
    left: 55px; top: 48px;
    font-size: 26px;
    font-weight: 700;
    color: var(--brand-blue);
  }
  .person-title {
    position: absolute;
    left: 55px; top: 82px;
    font-size: 18px;
    color: var(--brand-green);
  }
  .contact {
    position: absolute;
    left: 55px; top: 140px;
    font-size: 18px;
    line-height: 24px;
    color: var(--ink-grey);
    list-style: none;
  }
  .contact .company { margin-bottom: 0; }
  .contact .line { display: flex; align-items: center; gap: 8px; }
  .contact svg { width: 16px; height: 16px; fill: var(--brand-blue); flex: none; }
  .brand-mark {
    position: absolute;
    right: 50px; top: 255px;
    font-size: 40px;
    font-weight: 700;
    letter-spacing: 2px;
    color: var(--brand-blue);
  }
  .accent-band {
    position: absolute;
    left: 0; bottom: 0;
    width: 700px; height: 70px;
  }
</style>
</head>
<body>

  <section class="card card-back">
    <div class="brand-name">QV RUNNERS</div>
    <div class="brand-web">www.qvrunners.com</div>
  </section>

  <section class="card card-front">
    <h1 class="person-name">Thomas R. Wendall</h1>
    <p class="person-title">President</p>

    <ul class="contact">
      <li class="company">QVmotion</li>
      <li>20864 Lark Fenmore Parkway</li>
      <li>Cincinnati, Oh 45873</li>
      <li class="line">
        <svg viewBox="0 0 16 16" aria-hidden="true"><path d="M3 1h3l1.5 4-2 1.3a9 9 0 0 0 4.2 4.2L11 8.5 15 10v3a2 2 0 0 1-2 2A12 12 0 0 1 1 3a2 2 0 0 1 2-2z"/></svg>
        (513) 555-0147
      </li>
      <li class="line">
        <svg viewBox="0 0 16 16" aria-hidden="true"><path d="M1 3h14v1.2L8 9 1 4.2z"/><path d="M1 5.6 8 10.4l7-4.8V13H1z"/></svg>
        tom@qvrunners.com
      </li>
      <li class="line">
        <svg viewBox="0 0 16 16" aria-hidden="true"><path d="M8 1a5 5 0 0 0-5 5c0 4 5 9 5 9s5-5 5-9a5 5 0 0 0-5-5zm0 7a2 2 0 1 1 0-4 2 2 0 0 1 0 4z"/></svg>
        www.qvrunners.com
      </li>
    </ul>

    <div class="brand-mark">QV RUNNERS</div>

    <svg class="accent-band" viewBox="0 0 700 70" aria-hidden="true">
      <polygon points="0,30 200,30 215,70 0,70" fill="var(--brand-blue)"/>
      <polygon points="200,30 250,36 470,58 480,70 215,70" fill="var(--brand-green)"/>
      <polygon points="470,58 700,52 700,70 480,70" fill="var(--brand-blue)"/>
    </svg>
  </section>

</body>
</html>
```